Bar and Grill looking or a Responsive Web design

New Bar and Grill in the Toronto area just opened up and is looking for a new wordpress website to start off his business.

Their business revolves around a homey family, upbeat atmosphere. His cuisine is gourmet pub style food. Speciality are home made burgers. 90 Seat restaurant in a very diverse and high density neighbourhood.

Looking for a responsive web design that will focus on a key feature pages.

Homepage
- Navigation is easy and simple, emphasize easy navigation in Mobile view.
- Contact information is a click or touch away

About Page

Menu Page
-Menu styling to be responsive. Very simple navigation through different menus and then menu would appear.

Gallery

Contact page
- Map (not googlesk)
- Contact Details
- Contact/Feedback form

They do have a logo and will be uploaded.

We are open to any designs, as well as designs based off templates that have already been created.

Target Market(s)

Target audience is the varied. They are in an area that's densely populated and very diverse. Looking for a crowd that appreciates a setting for sports, good gourmet pub styled food and a home styled restaurant.

Industry/Entity Type

Restaurant

Colors

Designer to choose colors to be used in the design.

Requirements
Must have
• Menus have to have responsive design for both mobile and tablet/desktop.
Nice to have
• Easy access contact button on mobile view. That way it will act like a webapp so that mobile devices can take advantage of quick touches to get in contact.

```html
<!DOCTYPE html>
<html lang="en">
<head>
<meta charset="utf-8">
<title>The Millbrook – Gallery</title>
<link href="https://fonts.googleapis.com/css2?family=Open+Sans:wght@300;400;600;700;800&display=swap" rel="stylesheet">
<style>
  :root {
    --bar-dark: #252525;
    --bg-deep: #2a1a16;
    --bg-warm: #5a3a30;
    --panel: rgba(236, 236, 236, 0.95);
    --ink: #2f2f2f;
    --active: #222;
    --card: #ffffff;
    --rule: #2b2b2b;
    --social: #9c9c9c;
    --topbar-ink: #e6e6e6;
    --footer-ink: #c9c0bc;
  }
  * { box-sizing: border-box; margin: 0; padding: 0; }
  html, body { width: 1200px; height: 547px; overflow: hidden; }
  body {
    position: relative;
    font-family: "Open Sans", Arial, sans-serif;
    color: var(--ink);
  }
  .backdrop {
    position: absolute; inset: 0;
    background:
      radial-gradient(ellipse at 20% 70%, rgba(120,80,70,.55), transparent 60%),
      radial-gradient(ellipse at 85% 60%, rgba(110,90,85,.5), transparent 55%),
      linear-gradient(180deg, var(--bg-deep) 0%, var(--bg-warm) 55%, #4a3a36 100%);
  }
  .topbar {
    position: absolute; left: 0; top: 0; width: 1200px; height: 27px;
    background: var(--bar-dark);
    color: var(--topbar-ink); font-size: 12px;
  }
  .topbar .contact-list {
    position: absolute; right: 140px; top: 0; height: 27px;
    display: flex; align-items: center; gap: 22px; white-space: nowrap;
  }
  .topbar .item { display: flex; align-items: center; gap: 5px; letter-spacing: -.2px; }

  .sidebar {
    position: absolute; left: 248px; top: 43px; width: 134px; height: 328px;
    background: var(--panel); border-radius: 2px;
  }
  .brand { position: absolute; left: 14px; top: 16px; width: 106px; height: 66px; }
  .brand .bar { position: absolute; left: 0; width: 106px; height: 3px; background: var(--rule); }
  .brand .bar.top { top: 0; }
  .brand .bar.bottom { top: 63px; }
  .brand .name {
    position: absolute; left: 0; right: 0; top: 24px; text-align: center;
    font-weight: 800; font-size: 12px; line-height: 16px; white-space: nowrap;
    color: var(--ink);
  }
  .divider { position: absolute; left: 0; width: 134px; height: 3px; background: var(--rule); }
  .divider.upper { top: 96px; }
  .divider.lower { top: 271px; }

  .nav { position: absolute; left: 14px; top: 114px; width: 106px; list-style: none; }
  .nav li {
    height: 29px; line-height: 29px; text-align: center;
    font-size: 11.5px; font-weight: 700; color: var(--ink); position: relative;
  }
  .nav li::after {
    content: ""; position: absolute; left: 29px; bottom: 0; width: 48px;
    border-bottom: 1px dashed #b5b5b5;
  }
  .nav li.active { background: var(--active); color: #fff; height: 30px; line-height: 30px; }
  .nav li.active::after, .nav li:last-child::after, .nav li.before-active::after { display: none; }

  .social { position: absolute; left: 14px; top: 288px; display: flex; gap: 8px; }
  .social span { width: 22px; height: 21px; background: var(--social); border-radius: 2px; }

  .content {
    position: absolute; left: 397px; top: 43px; width: 555px; height: 459px;
    background: var(--panel); border-radius: 2px;
  }
  .content h1 {
    position: absolute; left: 0; right: 0; top: 14px; text-align: center;
    font-size: 28px; font-weight: 800; letter-spacing: -.3px; color: var(--ink);
  }
  .content .title-rule {
    position: absolute; left: 253px; top: 61px; width: 50px; border-bottom: 1px dashed #a8a8a8;
  }
  .card { position: absolute; width: 165px; height: 164px; background: var(--card); }
  .card .photo { display: block; width: 165px; height: 120px; }
  .card .label {
    height: 44px; line-height: 44px; text-align: center;
    font-size: 11.5px; font-weight: 700; color: var(--ink);
  }
  .c1 { left: 16px; } .c2 { left: 195px; } .c3 { left: 376px; }
  .r1 { top: 86px; } .r2 { top: 266px; }

  .photo.events { background: linear-gradient(135deg, #4a3c36 0%, #8a6a58 45%, #c9c2c4 70%, #5a4640 100%); }
  .photo.restaurant { background: linear-gradient(180deg, #7a2a1a 0%, #c8642a 35%, #6a3a22 65%, #3a2418 100%); }
  .photo.food { background: linear-gradient(180deg, #7a1010 0%, #d8a040 40%, #5a2a18 60%, #e0b45a 80%, #4a6a2a 100%); }
  .photo.beverages { background: linear-gradient(90deg, #1a1210 0%, #3a2418 45%, #c07a20 75%, #6a4018 100%); }
  .photo.matches { background: linear-gradient(180deg, #2a2a2a 0%, #8a3030 45%, #3a6a2a 75%, #2a5a1e 100%); }

  .footer {
    position: absolute; left: 397px; width: 555px; top: 516px; text-align: center;
    font-size: 10px; font-weight: 300; color: var(--footer-ink);
  }
</style>
</head>
<body>
  <div class="backdrop" role="img" aria-label="Dimly lit bar interior with seating and screens"></div>

  <header class="topbar">
    <div class="contact-list">
      <div class="item address">
        <svg width="8" height="11" viewBox="0 0 8 11"><path d="M4 0a4 4 0 0 0-4 4c0 3 4 7 4 7s4-4 4-7a4 4 0 0 0-4-4zm0 5.5A1.5 1.5 0 1 1 4 2.5a1.5 1.5 0 0 1 0 3z" fill="#e6e6e6"/></svg>
        <span>4870 Harbour Ave, Toronto, ON M5V 3K8</span>
      </div>
      <div class="item phone">
        <svg width="9" height="11" viewBox="0 0 9 11"><path d="M2 0l2 2.6-1.2 1.2c.6 1.4 1.5 2.6 2.6 3.4l1.2-1.1L9 8.2 7.6 10.6C3.5 10 .4 6 0 1.6z" fill="#e6e6e6"/></svg>
        <span>416-555-0173</span>
      </div>
    </div>
  </header>

  <aside class="sidebar">
    <div class="brand">
      <span class="bar top"></span>
      <span class="name">THE MILLBROOK</span>
      <span class="bar bottom"></span>
    </div>
    <span class="divider upper"></span>
    <ul class="nav">
      <li>HOME</li>
      <li>MENU</li>
      <li class="before-active">EVENTS +</li>
      <li class="active">GALLERY</li>
      <li>CONTACT</li>
    </ul>
    <span class="divider lower"></span>
    <div class="social" aria-label="Social links">
      <span></span><span></span><span></span><span></span>
    </div>
  </aside>

  <main class="content">
    <h1>GALLERY</h1>
    <span class="title-rule"></span>

    <div class="card c1 r1">
      <div class="photo events" role="img" aria-label="Fans cheering at the bar during a game"></div>
      <div class="label">EVENTS</div>
    </div>
    <div class="card c2 r1">
      <div class="photo restaurant" role="img" aria-label="Restaurant dining room with bar seating and screens"></div>
      <div class="label">THE RESTAURANT</div>
    </div>
    <div class="card c3 r1">
      <div class="photo food" role="img" aria-label="Homemade burger with cheese"></div>
      <div class="label">OUR FOOD</div>
    </div>
    <div class="card c1 r2">
      <div class="photo beverages" role="img" aria-label="Dark beer and a glass of whisky"></div>
      <div class="label">BEVERAGES</div>
    </div>
    <div class="card c2 r2">
      <div class="photo matches" role="img" aria-label="Football player running on the field"></div>
      <div class="label">LATEST MATCHES</div>
    </div>
  </main>

  <footer class="footer">© 2013 The Millbrook 4870. All Rights Reserved.</footer>
</body>
</html>
```